VELQUARTH - A modern gin bottle label

Design of a bottle label in a modern fresh design. The name of the gin is "VELQUARTH Hollow Batch K7". Please take a look at the velquarth.de website. on the main page of velquarth.de you can breathe the design direction here: 1) the taste of the gin should be composed of 10 botanicals ... an important scent note. ) a distinctive flavor is spicy and fresh 3.) The filling volume is 0.5 liters 4.) the alcohol content is 43% vol. 5.) the variety is called "dry gin" 6.) velquarth stands for "energy" and "love"

Target Market(s)

Alcohol consumer

Colors

Designer to choose colors to be used in the design.

Requirements
Must have
• the velquarth corporate logo must be included, the name of the gin is "VELQUARTH Hollow Batch K7"
Nice to have
• Please use the bottles template in the appendix. (The Black Bottles) they can use the saying "DESTILLED & BOTTLED BY OLD MARROW" in small letters

```html
<!DOCTYPE html>
<html lang="en">
<head>
<meta charset="utf-8">
<title>VELQUARTH Dry Gin – Hollow Batch K7 label</title>
<link rel="stylesheet" href="https://fonts.googleapis.com/css2?family=Bebas+Neue&family=Montserrat:wght@400;600&display=swap">
<style>
  :root {
    --backdrop: #bde0e7;
    --label-black: #0c0c0c;
    --splash-rust: #a8400f;
    --splash-deep: #8a3410;
    --ink-white: #eeeeee;
    --brand-orange: #f26a1b;
  }
  * { box-sizing: border-box; margin: 0; padding: 0; }
  html, body { width: 1200px; height: 900px; overflow: hidden; }
  body {
    background: var(--backdrop);
    display: flex;
    align-items: center;
    justify-content: center;
  }
  .label {
    position: relative;
    width: 480px;
    height: 726px;
    background: var(--label-black);
    color: var(--ink-white);
    overflow: hidden;
  }
  .label__splash {
    position: absolute;
    left: 90px;
    top: 200px;
    width: 310px;
    height: 400px;
    border-radius: 48% 52% 44% 56% / 40% 46% 54% 60%;
    background: radial-gradient(ellipse at 50% 45%, var(--splash-rust) 0%, var(--splash-deep) 62%, rgba(138,52,16,0) 72%);
  }
  .brand {
    position: absolute;
    top: 62px;
    left: 0;
    width: 100%;
    display: flex;
    align-items: center;
    justify-content: center;
    gap: 12px;
  }
  .brand__mark {
    width: 14px;
    height: 14px;
    background: var(--brand-orange);
  }
  .brand__name {
    font-family: "Montserrat", sans-serif;
    font-weight: 600;
    font-size: 27px;
    letter-spacing: 0.16em;
    color: var(--ink-white);
  }
  .variety {
    position: absolute;
    top: 228px;
    left: 0;
    width: 100%;
    text-align: center;
    font-family: "Bebas Neue", sans-serif;
    font-size: 158px;
    line-height: 1;
    letter-spacing: 0.02em;
    color: var(--ink-white);
  }
  .edition {
    position: absolute;
    top: 400px;
    left: 0;
    width: 100%;
    text-align: center;
    font-family: "Bebas Neue", sans-serif;
    font-size: 48px;
    letter-spacing: 0.06em;
    color: var(--ink-white);
  }
  .taste {
    position: absolute;
    top: 468px;
    left: 0;
    width: 100%;
    text-align: center;
    font-family: "Bebas Neue", sans-serif;
    font-size: 30px;
    letter-spacing: 0.08em;
    color: var(--ink-white);
  }
  .facts {
    position: absolute;
    top: 662px;
    left: 0;
    width: 100%;
    display: flex;
    justify-content: center;
    align-items: center;
    gap: 10px;
    font-family: "Montserrat", sans-serif;
    font-weight: 400;
    font-size: 21px;
    color: var(--ink-white);
  }
  .facts__divider {
    width: 2px;
    height: 26px;
    background: var(--ink-white);
  }
</style>
</head>
<body>
  <main class="label">
    <div class="label__splash" role="img" aria-label="Rust-orange paint splatter behind the product name"></div>

    <div class="brand">
      <span class="brand__mark"></span>
      <span class="brand__name">VELQUARTH</span>
    </div>

    <h1 class="variety">DRY GIN</h1>
    <p class="edition">HOLLOW BATCH K7</p>
    <p class="taste">FRESH &amp; SPICY</p>

    <p class="facts">
      <span>0.5 fl oz</span>
      <span class="facts__divider"></span>
      <span>43% alcohol</span>
    </p>
  </main>
</body>
</html>
```